■依頼の目的/概要
電子書籍の表紙デザインをお願いします。

経営者のための「黄金オフィス気学」
〜歴史に名を遺す名将や成功者はみんなやっていた〜

著者
経営者専属:開運鑑定士 夕凪みのり

★読者限定プレゼント→今すぐあなたや社員の吉方位が分かる「本命掛早見表と八宅盤」

■本の内容
経営者向けの経営サポート本として「ビジネス風水」を具体的にご紹介しています。
「まえがき、目次、本文、後書き」原稿をファイル添付していますので、まえがきや目次等見ていただき、内容の雰囲気をご確認いただけると嬉しいです。

筆者(私)はタロット歴20年の電話占い師(夕凪みのり)です。本書の著者の肩書きは↑にも書いておりますように「経営者専属:開運鑑定士 夕凪みのり」でお願い致します。

■デザイン要望
経営者に魅力を感じていただきやすくパッと目を引き、どのような本なのかが一目で分かりやすいデザインが望ましいです。基本全部おまかせです。是非デザイナーさんの魅力と才能を発揮していただけたらと思います。

その他何かご不明な点がございましたら、お気軽にご質問下さい。
よろしくお願いいたします。
【画像サイズ】※RLQより抜粋(電子書籍はLumoraです)
表紙ファイルの理想的な寸法は、2,560✖️1,600ピクセルです。
注:画像の寸法は、1,000✖️625ピクセル以上であることが必要です。
画像の最大の寸法は、10,000✖️10,000ピクセルです。

Zentaro(Lumora)に表示された際はかなり小さくなる事を踏まえ、他の経営者向けの本と並んだ時、目が止まりやすい一冊になるか?という点を意識し、選ばさせて頂きました。

表紙デザインの色や見た目のインパクトと文字の分かりやすさ、サブタイトルまでしっかりアピールされている所が気に入りました。

クラフターの皆様、この度はコンペにご参加いただきまして誠にありがとうございました。
本当に素晴らしいデザインばかりで、正直選考はとても難航いたしました。

今回は沢山のご提案の中から1つを選ぶことがとても難しかった為「他の経営者向けの本と並んだ時、目が止まりやすい一冊になるか?内容が分かりやすいか?」を軸に、著者仲間30名にアンケートを実施し当選作品を決定させて頂きました。

改めまして、皆様の才能を発揮して頂き素晴らしい作品をご提案頂きました事、心より感謝申し上げます。誠にありがとうございました。

```html
<!DOCTYPE html>
<html lang="ja">
<head>
<meta charset="UTF-8">
<title>経営者のための黄金オフィス気学</title>
<link href="https://fonts.googleapis.com/css2?family=Noto+Serif+JP:wght@600;700;900&family=Noto+Sans+JP:wght@500;700;900&family=Great+Vibes&display=swap" rel="stylesheet">
<style>
  :root{
    --ink:#111111;
    --gold:#b88a2e;
    --gold-band:#c9a24e;
    --paper:#ffffff;
    --faint:#e6e6e6;
  }
  *{margin:0;padding:0;box-sizing:border-box;}
  html,body{width:750px;height:1200px;overflow:hidden;background:var(--paper);}
  .cover{position:relative;width:750px;height:1200px;overflow:hidden;background:var(--paper);
    font-family:"Noto Serif JP",serif;color:var(--ink);}
  .lead{position:absolute;top:30px;left:0;width:750px;text-align:center;font-size:72px;font-weight:700;letter-spacing:2px;line-height:1.2;}
  .lead .accent{color:var(--gold);}
  .lead-rule{position:absolute;top:138px;left:45px;width:660px;height:30px;}
  .script-bg{position:absolute;top:470px;left:20px;font-family:"Great Vibes",cursive;font-size:76px;color:var(--faint);
    transform:rotate(-4deg);white-space:nowrap;}
  .title-big{position:absolute;font-weight:900;font-size:250px;line-height:1;}
  .t-ki{left:-6px;top:190px;}
  .t-gaku{left:-6px;top:482px;}
  .t-ou{left:500px;top:190px;}
  .t-kin{left:500px;top:478px;}
  .title-kana{position:absolute;left:380px;top:195px;writing-mode:vertical-rl;font-size:96px;font-weight:700;
    color:var(--gold);letter-spacing:6px;line-height:1;}
  .emblem{position:absolute;left:248px;top:645px;width:130px;height:130px;border-radius:50%;
    background:radial-gradient(circle at 40% 40%,#3a3a3a,#111);border:3px solid var(--ink);}
  .author{position:absolute;left:448px;top:790px;font-family:"Noto Sans JP",sans-serif;}
  .author-role{font-size:18px;font-weight:700;line-height:1.3;}
  .author-name{font-size:30px;font-weight:700;font-family:"Noto Serif JP",serif;margin-top:2px;margin-left:80px;letter-spacing:2px;line-height:1.2;}
  .deco{position:absolute;}
  .band{position:absolute;left:0;top:850px;width:750px;height:350px;background:var(--gold-band);}
  .subtitle{position:absolute;left:40px;top:868px;color:#fff;font-family:"Noto Sans JP",sans-serif;font-weight:700;
    font-size:54px;line-height:1.24;letter-spacing:1px;}
  .gift{position:absolute;left:45px;top:1015px;width:662px;height:160px;background:#fff;border-radius:16px;}
  .gift-tag{position:absolute;left:20px;top:20px;width:145px;height:120px;border-radius:12px;background:var(--gold-band);
    color:#fff;font-family:"Noto Sans JP",sans-serif;font-weight:700;font-size:26px;line-height:1.35;
    display:flex;align-items:center;justify-content:center;text-align:center;}
  .gift-arrow{position:absolute;left:176px;top:58px;width:40px;height:44px;}
  .gift-lead{position:absolute;left:228px;top:26px;font-family:"Noto Sans JP",sans-serif;font-weight:700;font-size:23px;line-height:1.3;}
  .gift-item{position:absolute;left:212px;top:68px;font-family:"Noto Sans JP",sans-serif;font-weight:900;font-size:36px;line-height:1.3;
    color:var(--gold);letter-spacing:1px;white-space:nowrap;}
</style>
</head>
<body>
<main class="cover">
  <div class="script-bg" aria-hidden="true">Best golden office kigaku</div>

  <h2 class="lead"><span class="accent">経営者</span>のための</h2>
  <svg class="lead-rule" viewBox="0 0 660 30" aria-hidden="true">
    <polyline points="0,6 305,6 330,26 355,6 660,6" fill="none" stroke="#111" stroke-width="4"/>
  </svg>

  <h1 class="title" aria-label="黄金オフィス気学">
    <span class="title-big t-ou">黄</span>
    <span class="title-big t-kin">金</span>
    <span class="title-kana">オフィス</span>
    <span class="title-big t-ki">気</span>
    <span class="title-big t-gaku">学</span>
  </h1>

  <div class="emblem" role="img" aria-label="陰陽の紋章"></div>

  <svg class="deco" style="left:12px;top:806px" width="100" height="30" aria-hidden="true">
    <rect x="30" y="0" width="40" height="7" fill="#111"/>
    <rect x="0" y="18" width="100" height="7" fill="#111"/>
  </svg>

  <div class="author">
    <p class="author-role">経営者専属:開運鑑定士</p>
    <p class="author-name">夕凪みのり</p>
  </div>

  <section class="band"></section>
  <svg class="deco" style="left:640px;top:892px" width="80" height="38" aria-hidden="true">
    <rect x="0" y="0" width="80" height="6" fill="#111"/>
    <rect x="22" y="14" width="36" height="6" fill="#fff"/>
    <rect x="8" y="28" width="64" height="6" fill="#111"/>
  </svg>

  <p class="subtitle">歴史に名を遺す名将や<br>成功者はみんなやっていた</p>

  <div class="gift">
    <div class="gift-tag">読者限定<br>プレゼント</div>
    <svg class="gift-arrow" viewBox="0 0 40 44" aria-hidden="true">
      <polyline points="4,4 20,22 4,40" fill="none" stroke="#b88a2e" stroke-width="5"/>
      <polyline points="18,4 34,22 18,40" fill="none" stroke="#b88a2e" stroke-width="5"/>
    </svg>
    <p class="gift-lead">今すぐあなたや社員の吉方位が分かる</p>
    <p class="gift-item">「本命掛早見表と八宅盤」</p>
  </div>
</main>
</body>
</html>
```